Tambrook copiers needs flyer for the Corvane Trade expo

A flyer to hand out had the Corvane Trade expo in Melbourne. I am am happy with the layout attached , but i need a claen ( no watermarks) background for the top half of the fist page. It must have one of the copiers attached in the photo

```html
<!DOCTYPE html>
<html lang="en">
<head>
<meta charset="utf-8">
<title>Tambrook Copiers – Corvane Trade expo flyer</title>
<link href="https://fonts.googleapis.com/css2?family=Montserrat:ital,wght@0,200;0,400;0,500;0,600;0,700;0,800;1,700;1,800&display=swap" rel="stylesheet">
<style>
  :root {
    --red: #e2211c;
    --red-mid: #d11d1f;
    --red-dark: #b8191c;
    --ink: #111111;
    --text: #333333;
    --grey-col: #efefef;
    --rule: #555555;
    --paper: #ffffff;
  }
  * { box-sizing: border-box; margin: 0; padding: 0; }
  html, body { width: 848px; height: 1200px; overflow: hidden; background: var(--paper); }
  body { font-family: 'Montserrat', sans-serif; color: var(--text); position: relative; }

  .brand { position: absolute; left: 43px; top: 78px; display: flex; align-items: center; gap: 16px; }
  .brand-mark { width: 34px; height: 34px; background: var(--red); }
  .brand-name { font-weight: 800; font-size: 60px; line-height: 1; color: var(--ink); letter-spacing: -1px; text-transform: uppercase; }
  .brand-name span { display: block; }

  .copier-photo { position: absolute; left: 406px; top: 140px; width: 420px; height: 450px;
    background: radial-gradient(ellipse at 55% 45%, #dfe2e6 0%, #c9ccd1 45%, #ffffff 75%); border-radius: 6px; }

  .features { position: absolute; left: 43px; top: 350px; list-style: none; }
  .features li { width: 352px; padding: 0 0 7px; margin-bottom: 22px; border-bottom: 3px solid var(--red);
    font-size: 14px; font-weight: 500; text-transform: uppercase; letter-spacing: 0.3px; color: var(--ink); white-space: nowrap; line-height: 1.2; }

  .tagline-bar-left { position: absolute; left: 0; top: 606px; width: 150px; height: 38px; background: var(--red); }
  .tagline-strong { position: absolute; left: 157px; top: 598px; font-size: 58px; font-weight: 700; color: var(--ink); line-height: 1; white-space: nowrap; }
  .tagline-light { position: absolute; left: 331px; top: 651px; font-size: 59px; font-weight: 200; color: var(--ink); line-height: 1; white-space: nowrap; }
  .tagline-bar-right { position: absolute; left: 708px; top: 660px; width: 140px; height: 41px; background: var(--red); }

  .plans { position: absolute; left: 50px; top: 751px; width: 752px; height: 406px; display: grid; grid-template-columns: repeat(3, 1fr);
    grid-template-rows: 406px; box-shadow: 0 0 6px rgba(0,0,0,0.12); }
  .plan { display: flex; flex-direction: column; border-top: 7px solid var(--red); height: 406px; overflow: hidden; }
  .plan--medium { background: var(--grey-col); border-top-color: var(--red-mid); }
  .plan--colour { border-top-color: var(--red-dark); }
  .plan-head { height: 68px; text-align: center; padding-top: 14px; }
  .plan-title { font-size: 24px; font-weight: 700; color: var(--ink); line-height: 1; }
  .plan-sub { font-size: 16px; font-weight: 400; color: var(--text); text-transform: uppercase; }
  .plan-price { height: 82px; background: var(--red); color: #fff; display: flex; align-items: center; padding-left: 22px; gap: 10px; }
  .plan--medium .plan-price { background: var(--red-mid); }
  .plan--colour .plan-price { background: var(--red-dark); }
  .price-sign { font-size: 28px; font-weight: 700; }
  .price-amount { font-size: 52px; font-weight: 800; font-style: italic; line-height: 1; }
  .price-note { font-size: 11px; font-weight: 500; line-height: 1.2; margin-top: -8px; }
  .plan-details { list-style: none; padding: 16px 16px 0 22px; flex: 1; min-height: 0; }
  .plan-details li { position: relative; padding-left: 20px; font-size: 14px; line-height: 1.35; margin-bottom: 8px; }
  .plan-details li::before { content: ""; position: absolute; left: 2px; top: 8px; width: 5px; height: 5px; border-radius: 50%; background: var(--text); }
  .plan-daily { margin: 0 12px 10px 16px; border-top: 2px solid var(--rule); padding-top: 6px; height: 84px; flex: none; }
  .daily-lead { font-size: 14px; font-weight: 600; color: var(--ink); }
  .daily-price { display: flex; align-items: center; justify-content: center; gap: 12px; color: var(--ink); margin-top: 0; }
  .daily-price .price-sign { font-size: 26px; font-style: italic; }
  .daily-price .price-amount { font-size: 48px; }
  .daily-price sup { font-size: 24px; vertical-align: 20px; }
  .daily-price .price-note { margin-top: 10px; }
</style>
</head>
<body>
  <header class="brand">
    <div class="brand-mark"></div>
    <div class="brand-name"><span>Tambrook</span><span>Copiers</span></div>
  </header>

  <div class="copier-photo" role="img" aria-label="Freestanding A3/A4 colour multifunction copier with document feeder and paper drawers"></div>

  <ul class="features">
    <li>Freestanding A3/A4 colour printer</li>
    <li>Includes all toner &amp; service</li>
    <li>Change plans to suit your needs</li>
  </ul>

  <div class="tagline-bar-left"></div>
  <div class="tagline-strong">NO LOCK-IN</div>
  <div class="tagline-light">CONTRACTS</div>
  <div class="tagline-bar-right"></div>

  <section class="plans">
    <article class="plan plan--small">
      <div class="plan-head"><div class="plan-title">SMALL</div><div class="plan-sub">Business plan</div></div>
      <div class="plan-price"><span class="price-sign">$</span><span class="price-amount">150</span><span class="price-note">+GST<br>per Month</span></div>
      <ul class="plan-details">
        <li>Includes printer &amp; 3000 B&amp;W pages p/m</li>
        <li>Excess B&amp;W pages are 5c +GST and colour pages are 9c +GST</li>
      </ul>
      <div class="plan-daily"><div class="daily-lead">That's only</div>
        <div class="daily-price"><span class="price-sign">$</span><span class="price-amount">5</span><span class="price-note">+GST<br>per Day</span></div></div>
    </article>
    <article class="plan plan--medium">
      <div class="plan-head"><div class="plan-title">MEDIUM</div><div class="plan-sub">Business plan</div></div>
      <div class="plan-price"><span class="price-sign">$</span><span class="price-amount">210</span><span class="price-note">+GST<br>per Month</span></div>
      <ul class="plan-details">
        <li>Includes printer &amp; 6000 B&amp;W pages p/m</li>
        <li>Excess B&amp;W pages are 3.5c +GST and colour pages are 9c +GST</li>
      </ul>
      <div class="plan-daily"><div class="daily-lead">That's just</div>
        <div class="daily-price"><span class="price-sign">$</span><span class="price-amount">7</span><span class="price-note">+GST<br>per Day</span></div></div>
    </article>
    <article class="plan plan--colour">
      <div class="plan-head"><div class="plan-title">DISCOUNTED</div><div class="plan-sub">Colour plan</div></div>
      <div class="plan-price"><span class="price-sign">$</span><span class="price-amount">280</span><span class="price-note">+GST<br>per Month</span></div>
      <ul class="plan-details">
        <li>Includes printer &amp; 4000 colour pages p/m</li>
        <li>Excess B&amp;W pages are 7c +GST</li>
        <li>Discounts for high volume users</li>
      </ul>
      <div class="plan-daily"><div class="daily-lead">Less than</div>
        <div class="daily-price"><span class="price-sign">$</span><span class="price-amount">9.<sup>50</sup></span><span class="price-note">+GST<br>per Day</span></div></div>
    </article>
  </section>
</body>
</html>
```